Business Card Design

We Import cars and commercial vehicles, we have been in business around 12 years, we are based in Christchurch, New Zealand.
I really like the web address on card, possibly right along the bottom of the card?
We specialize in commercial vans, maybe worth a mention?
The logo has the name in it so probably don't need to have twice?

I really like a clean smart look, not too cluttered

Industry/Entity Type

Business

Contact Information for Business Card

RQL TOKYO IMPORTS, Derek Holloway, Managing Director
web address: www.rqlmotorsnz.com
cell phone. 021 485 912

Requirements
Must have
• the logo, and all the contact details.

Forgot to add my email address, derek@rqlmotorsnz.com
Nice to have
• Just thinking as the card is looking a little empty maybe somewhere written what we do? 'Specializing in commercial vans'
Not sure but we import Japanese vehicles, possibly adding some brands like Velkara Poremo Ketsu Brivon etc? Not sure on that one.

```html
<!DOCTYPE html>
<html lang="en">
<head>
<meta charset="utf-8">
<title>RQL Tokyo Imports – Business Card</title>
<link rel="stylesheet" href="https://fonts.googleapis.com/css2?family=Arimo:wght@400;700&display=swap">
<style>
  :root {
    --page: #1d1d1e;
    --card-grey: #4a4a4c;
    --band-black: #0b0b0b;
    --brand-red: #c8202a;
    --text-white: #f2f2f2;
    --text-soft: #a9a9ab;
    --logo-sub: #b8b8ba;
    --van-tone: #d9d9d9;
    --van-shadow: #1a1a1a;
    --ketsu-blue: #4fb3e0;
  }
  html, body {
    margin: 0;
    padding: 0;
    width: 1200px;
    height: 900px;
    overflow: hidden;
    background: var(--page);
    font-family: "Arimo", Arial, sans-serif;
  }
  .canvas {
    position: relative;
    width: 1200px;
    height: 900px;
    display: flex;
    align-items: center;
    justify-content: center;
  }
  .card {
    position: relative;
    width: 840px;
    height: 480px;
    background: var(--card-grey);
    overflow: hidden;
    box-shadow: 0 10px 30px rgba(0,0,0,.45);
  }
  .brand-logo {
    position: absolute;
    left: 200px;
    top: 92px;
    width: 250px;
    text-align: right;
    color: var(--brand-red);
    font-weight: 700;
    font-size: 34px;
    line-height: 1.05;
    letter-spacing: 1px;
  }
  .van-illustration {
    position: absolute;
    left: 465px;
    top: 40px;
    width: 250px;
    height: 170px;
    border-radius: 10px;
    background: linear-gradient(180deg, var(--van-tone) 0%, #bdbdbd 65%, var(--van-shadow) 100%);
  }
  .tagline {
    position: absolute;
    right: 50px;
    top: 270px;
    margin: 0;
    color: var(--text-white);
    font-size: 19px;
    font-weight: 400;
  }
  .contact-band {
    position: absolute;
    left: 0;
    bottom: 0;
    width: 100%;
    height: 155px;
    background: var(--band-black);
  }
  .person {
    position: absolute;
    left: 40px;
    top: 18px;
    display: flex;
    align-items: baseline;
    gap: 18px;
  }
  .person-name {
    margin: 0;
    color: var(--brand-red);
    font-size: 32px;
    font-weight: 400;
  }
  .person-role {
    color: var(--text-white);
    font-size: 17px;
  }
  .contact-details {
    position: absolute;
    left: 40px;
    top: 72px;
    display: flex;
    gap: 26px;
    color: var(--text-soft);
    font-size: 13px;
  }
  .makes {
    position: absolute;
    right: 36px;
    top: 66px;
    display: flex;
    gap: 26px;
  }
  .make {
    display: flex;
    flex-direction: column;
    align-items: center;
    gap: 6px;
    font-size: 12px;
    font-weight: 700;
    letter-spacing: .5px;
  }
  .make-dot {
    width: 34px;
    height: 34px;
    border-radius: 50%;
    background: #d6d6d6;
  }
  .make--velkara { color: var(--brand-red); }
  .make--poremo { color: var(--text-white); }
  .make--ketsu { color: var(--ketsu-blue); }
</style>
</head>
<body>
<main class="canvas">
  <article class="card">
    <div class="brand-logo">RQL TOKYO IMPORTS</div>
    <div class="van-illustration" role="img" aria-label="White commercial van illustration in black and white"></div>
    <p class="tagline">Specializing in commercial vans</p>

    <section class="contact-band">
      <div class="person">
        <h1 class="person-name">Derek Holloway</h1>
        <span class="person-role">Managing Director</span>
      </div>
      <div class="contact-details">
        <span class="contact-web">www.rqlmotorsnz.com</span>
        <span class="contact-phone">cell phone. 021 485 912</span>
        <span class="contact-email">derek@rqlmotorsnz.com</span>
      </div>
      <div class="makes">
        <div class="make make--velkara"><span class="make-dot"></span>VELKARA</div>
        <div class="make make--poremo"><span class="make-dot"></span>POREMO</div>
        <div class="make make--ketsu"><span class="make-dot"></span>KETSU</div>
      </div>
    </section>
  </article>
</main>
</body>
</html>
```